Business Card Design

We Need a business card design for my company based in Tv Radio and music Productions and hunt Talent.

Industry/Entity Type

Business

Contact Information for Business Card

BrentaVue Production's, Teodor Vignoles,Cell Phone 318 4957310
Musician, Productor, Hunt Talent. Miami Fla. www.brentavue.net Mail. teodorvignoles@mailvana.com

```html
<!DOCTYPE html>
<html lang="en">
<head>
<meta charset="utf-8">
<title>BrentaVue Production's – Business Card</title>
<link rel="stylesheet" href="https://fonts.googleapis.com/css2?family=Questrial&display=swap">
<style>
  :root {
    --yellow: #fdd73a;
    --purple: #6b479a;
    --ink: #231f20;
    --paper: #ffffff;
  }
  html, body {
    margin: 0;
    padding: 0;
    overflow: hidden;
    background: var(--paper);
  }
  .card {
    position: relative;
    width: 1200px;
    height: 702px;
    background: var(--paper);
    overflow: hidden;
    font-family: "Questrial", sans-serif;
    color: var(--ink);
  }
  .band { position: absolute; left: 0; width: 100%; }
  .band--yellow-top { top: 0; height: 52px; background: var(--yellow); }
  .band--purple-top { top: 65px; height: 12px; background: var(--purple); }
  .band--purple-bottom { top: 623px; height: 13px; background: var(--purple); }
  .band--yellow-bottom { top: 649px; height: 53px; background: var(--yellow); }

  .brand-mark {
    position: absolute;
    left: 90px;
    top: 320px;
    width: 270px;
    text-align: center;
    font-size: 36px;
    line-height: 1;
    color: var(--purple);
  }

  .info {
    position: absolute;
    left: 415px;
    width: 719px;
    text-align: center;
    line-height: 1;
  }
  .company { top: 120px; font-size: 47px; margin: 0; font-weight: 400; }
  .person { top: 182px; font-size: 47px; margin: 0; font-weight: 400; color: var(--purple); }
  .rule {
    position: absolute;
    left: 415px;
    width: 719px;
    height: 2px;
    background: var(--ink);
  }
  .rule--upper { top: 272px; }
  .rule--lower { top: 506px; }
  .contact {
    top: 307px;
    margin: 0;
    font-style: normal;
  }
  .contact__line { display: block; }
  .contact__phone { font-size: 48px; margin-bottom: 12px; }
  .contact__web { font-size: 40px; margin-bottom: 16px; }
  .contact__mail { font-size: 37px; }

  .services {
    position: absolute;
    left: 413px;
    width: 721px;
    top: 543px;
    margin: 0;
    display: flex;
    justify-content: space-between;
    font-size: 44px;
    line-height: 1;
  }
  .services__sep { color: var(--purple); }
</style>
</head>
<body>
<main class="card">
  <div class="band band--yellow-top"></div>
  <div class="band band--purple-top"></div>

  <div class="brand-mark" role="img" aria-label="BrentaVue logo">BrentaVue</div>

  <h1 class="info company">BrentaVue Production's</h1>
  <h2 class="info person">Teodor Vignoles</h2>

  <div class="rule rule--upper"></div>

  <address class="info contact">
    <span class="contact__line contact__phone">318 4957310</span>
    <span class="contact__line contact__web">www.brentavue.net</span>
    <span class="contact__line contact__mail">teodorvignoles@mailvana.com</span>
  </address>

  <div class="rule rule--lower"></div>

  <p class="services">
    <span>Musician</span>
    <span class="services__sep">-</span>
    <span>Productor</span>
    <span class="services__sep">-</span>
    <span>Hunt Talent</span>
  </p>

  <div class="band band--purple-bottom"></div>
  <div class="band band--yellow-bottom"></div>
</main>
</body>
</html>
```